Custom Office Whiteboard for Staff

I need a custom whiteboard layout design. All fields are contained in the attached images along with artwork requirements including required bleed. Size will be 1200mm x 900mm.

Feel free to make is more visually appealing than this draft.

Use colors blue, black and white to keep company feel.

Font styles to use
Sans Serif

Colors
ffffff
000000
33a6d7

```html
<!DOCTYPE html>
<html lang="en">
<head>
<meta charset="utf-8">
<title>Highdrift Ballooning – Staff Whiteboard</title>
<link href="https://fonts.googleapis.com/css2?family=PT+Sans+Narrow:wght@400;700&display=swap" rel="stylesheet">
<style>
  :root {
    --blue: #33a6d7;
    --blue-soft: #e4f2fa;
    --blue-line: #c3dceb;
    --ink: #000000;
    --text: #222222;
    --frame: #3a3a3a;
    --paper: #ffffff;
    --backdrop: #ffffff;
  }
  * { box-sizing: border-box; margin: 0; padding: 0; }
  html, body { width: 1200px; height: 900px; overflow: hidden; background: var(--backdrop); }
  body { position: relative; font-family: "PT Sans Narrow", "Arial Narrow", sans-serif; color: var(--text); }

  .board { position: absolute; left: 95px; top: 70px; width: 1030px; height: 770px; background: var(--paper); }

  /* header */
  .brand { position: absolute; left: 145px; top: 118px; display: flex; align-items: center; gap: 12px; }
  .brand-dot { width: 34px; height: 34px; border-radius: 50%; background: var(--blue); }
  .brand-name { font-weight: 700; font-size: 62px; line-height: 1; color: var(--ink); letter-spacing: 1px; }
  .header-band { position: absolute; left: 520px; top: 122px; width: 557px; height: 76px;
    background: linear-gradient(90deg, rgba(51,166,215,0.04), rgba(51,166,215,0.22) 45%, rgba(51,166,215,0.16)); }
  .header-text { position: absolute; right: 133px; top: 126px; text-align: right; color: var(--text); }
  .company { font-weight: 700; font-size: 27px; line-height: 30px; }
  .credentials, .contact { font-weight: 700; font-size: 13.5px; line-height: 20px; }
  .header-rule { position: absolute; left: 142px; top: 208px; width: 935px; height: 2px; background: var(--blue); }

  /* panels */
  .panel { position: absolute; border: 1.5px solid var(--frame); border-radius: 9px; }
  .panel-title { position: absolute; top: -15px; left: 14px; padding: 0 8px; background: var(--paper);
    display: flex; align-items: center; gap: 6px; font-weight: 700; font-size: 22px; line-height: 26px; color: var(--text); }
  .panel-title::before { content: ""; width: 12px; height: 12px; border-radius: 50%; background: var(--blue); }
  .panel-title.centered { left: 50%; transform: translateX(-50%); }

  .crew { left: 142px; top: 252px; width: 683px; height: 301px; }
  .notes { left: 831px; top: 252px; width: 246px; height: 301px; }
  .six { left: 142px; top: 574px; width: 246px; height: 221px; }
  .twelve { left: 396px; top: 574px; width: 246px; height: 221px; }
  .schedule { left: 650px; top: 574px; width: 427px; height: 221px; }

  table.grid { position: absolute; left: 5px; top: 17px; border-collapse: collapse; table-layout: fixed; }
  .grid th { background: var(--blue); color: var(--paper); font-weight: 700; font-size: 11.5px; line-height: 11px;
    height: 31px; padding: 0 6px; text-align: center; border-bottom: 3px solid var(--paper); }
  .grid th.left { text-align: left; }
  .grid td { height: 20px; padding: 0 6px; font-weight: 700; font-size: 11.5px; color: var(--text);
    border-right: 2px solid var(--blue-line); white-space: nowrap; }
  .grid td:last-child { border-right: none; }
  .grid tbody tr:nth-child(odd) td { background: var(--paper); }
  .grid tbody tr:nth-child(even) td { background: var(--blue-soft); }
  .grid td.center { text-align: center; }
  .crew .grid tbody tr:nth-child(odd) td { background: var(--blue-soft); }
  .crew .grid tbody tr:nth-child(even) td { background: var(--paper); }
</style>
</head>
<body>
  <div class="board"></div>

  <header>
    <div class="brand"><span class="brand-dot"></span><span class="brand-name">Highdrift</span></div>
    <div class="header-band" role="img" aria-label="Soft blue band with faint balloon pattern"></div>
    <div class="header-text">
      <p class="company">Skyward Envelope Co Pty Ltd T/A Highdrift Ballooning</p>
      <p class="credentials">CASA AOC: S518204,&nbsp; Certificate of Approval: 4861</p>
      <p class="contact">hello@highdriftballooning.com.au,&nbsp; www.highdriftballooning.com.au, phone 1300 555 019</p>
    </div>
    <div class="header-rule"></div>
  </header>

  <section class="panel crew">
    <h2 class="panel-title">Flight / Ground Crew</h2>
    <table class="grid">
      <colgroup><col style="width:125px"><col style="width:67px"><col style="width:60px"><col style="width:56px"><col style="width:68px"><col style="width:69px"><col style="width:67px"><col style="width:88px"><col style="width:66px"></colgroup>
      <thead><tr><th class="left">Crew Name</th><th>License Class</th><th>Medical</th><th>BFR</th><th>Instructor Rating</th><th>CAO 20.11</th><th>DAMP</th><th>Maintenance Authority</th><th>ASIC</th></tr></thead>
      <tbody>
        <tr><td></td><td></td><td></td><td></td><td></td><td></td><td></td><td></td><td></td></tr>
        <tr><td></td><td></td><td></td><td></td><td></td><td></td><td></td><td></td><td></td></tr>
        <tr><td></td><td></td><td></td><td></td><td></td><td></td><td></td><td></td><td></td></tr>
        <tr><td></td><td></td><td></td><td></td><td></td><td></td><td></td><td></td><td></td></tr>
        <tr><td></td><td></td><td></td><td></td><td></td><td></td><td></td><td></td><td></td></tr>
        <tr><td></td><td></td><td></td><td></td><td></td><td></td><td></td><td></td><td></td></tr>
        <tr><td></td><td></td><td></td><td></td><td></td><td></td><td></td><td></td><td></td></tr>
        <tr><td></td><td></td><td></td><td></td><td></td><td></td><td></td><td></td><td></td></tr>
        <tr><td></td><td></td><td></td><td></td><td></td><td></td><td></td><td></td><td></td></tr>
        <tr><td></td><td></td><td></td><td></td><td></td><td></td><td></td><td></td><td></td></tr>
        <tr><td></td><td></td><td></td><td></td><td></td><td></td><td></td><td></td><td></td></tr>
        <tr><td></td><td></td><td></td><td></td><td></td><td></td><td></td><td></td><td></td></tr>
      </tbody>
    </table>
  </section>

  <section class="panel notes">
    <h2 class="panel-title centered">NOTES</h2>
  </section>

  <section class="panel six">
    <h2 class="panel-title">6 Monthly Tasks</h2>
    <table class="grid">
      <colgroup><col style="width:132px"><col style="width:97px"></colgroup>
      <thead><tr><th class="left">Task</th><th>Due Date</th></tr></thead>
      <tbody>
        <tr><td>Operations Manual</td><td></td></tr>
        <tr><td>Staff Meeting</td><td></td></tr>
        <tr><td>SMS Meeting</td><td></td></tr>
        <tr><td>Fire Extinguisher Inspection</td><td></td></tr>
        <tr><td>Flight Instrument Inspection</td><td></td></tr>
        <tr><td></td><td></td></tr>
        <tr><td></td><td></td></tr>
        <tr><td></td><td></td></tr>
      </tbody>
    </table>
  </section>

  <section class="panel twelve">
    <h2 class="panel-title">12 Monthly Tasks</h2>
    <table class="grid">
      <colgroup><col style="width:132px"><col style="width:97px"></colgroup>
      <thead><tr><th class="left">Task</th><th>Due Date</th></tr></thead>
      <tbody>
        <tr><td>COA Internal Audit</td><td></td></tr>
        <tr><td>SMS Audit</td><td></td></tr>
        <tr><td>Fatigue Training</td><td></td></tr>
        <tr><td>CAO 20.11</td><td></td></tr>
        <tr><td></td><td></td></tr>
        <tr><td></td><td></td></tr>
        <tr><td></td><td></td></tr>
        <tr><td></td><td></td></tr>
      </tbody>
    </table>
  </section>

  <section class="panel schedule">
    <h2 class="panel-title">Balloon Annual / Periodic Schedule</h2>
    <table class="grid">
      <colgroup><col style="width:83px"><col style="width:97px"><col style="width:121px"><col style="width:109px"></colgroup>
      <thead><tr><th class="left">Balloon</th><th>Type</th><th>Annual Date</th><th>Periodic Time</th></tr></thead>
      <tbody>
        <tr><td>VH-QZA</td><td class="center">Aer D90</td><td></td><td></td></tr>
        <tr><td>VH-QZB</td><td class="center">Aer E180</td><td></td><td></td></tr>
        <tr><td>VH-QZC</td><td class="center">Aer E240</td><td></td><td></td></tr>
        <tr><td>VH-QZD</td><td class="center">Aer B400</td><td></td><td></td></tr>
        <tr><td>VH-QZE</td><td class="center">Aer G450</td><td></td><td></td></tr>
        <tr><td></td><td></td><td></td><td></td></tr>
        <tr><td></td><td></td><td></td><td></td></tr>
        <tr><td></td><td></td><td></td><td></td></tr>
      </tbody>
    </table>
  </section>
</body>
</html>
```